Crestline 14 Industrial Park Needs Website

We are looking for a website for a new project we are working on.
Project does not have a logo so just use text. Needs to be responsive and mobile friendly for all browsers and coded for both Android & IOS. SEO is also important. Want something visually grabbing that displays growth, quality and confidence.
WordPress or Joomla – must be desktop and mobile friendly with fast page load speed. Need the ability to edit ourselves.
See attached website brief for further information.
Land Sale/Lease/Development
Coded - Design and coding required
4 page

```html
<!DOCTYPE html>
<html lang="en">
<head>
<meta charset="utf-8">
<title>Crestline 14 Industrial Park</title>
<link href="https://fonts.googleapis.com/css2?family=Unbounded:wght@800;900&family=Montserrat:wght@400;500;600;700&display=swap" rel="stylesheet">
<style>
:root{
  --ink:#141414;
  --blue:#00b4e6;
  --teal:#00d4c2;
  --grey:#f2f2f2;
  --mint:#effdf6;
  --pale:#d8f6f4;
  --text:#3a3a3a;
  --white:#ffffff;
}
*{margin:0;padding:0;box-sizing:border-box}
html,body{width:1200px;height:4860px;overflow:hidden}
body{font-family:"Montserrat",sans-serif;color:var(--text);background:var(--white);position:relative}
.abs{position:absolute}
.display{font-family:"Unbounded",sans-serif;font-weight:900;color:var(--ink);text-transform:uppercase;letter-spacing:.5px;line-height:1}
.accent{color:var(--blue)}
.btn{display:inline-block;background:var(--blue);color:var(--white);font-size:9px;font-weight:700;text-transform:uppercase;letter-spacing:.6px;padding:11px 14px;text-decoration:none}
.btn--gradient{background:linear-gradient(90deg,var(--blue),var(--teal))}
.photo{display:block}

/* hero */
.hero{left:0;top:0;width:1200px;height:612px;background:var(--grey)}
.hero__photo{left:600px;top:0;width:600px;height:612px;background:linear-gradient(160deg,#1c64c8 0%,#5aa5e8 35%,#2b4f8a 60%,#5c7a3a 85%,#3e5a26 100%)}
.nav{left:187px;top:26px;width:826px;height:61px;background:var(--white);display:flex;align-items:center;padding:0 24px;box-shadow:0 2px 10px rgba(0,0,0,.05)}
.logo{font-family:"Unbounded",sans-serif;font-weight:900;font-size:19px;color:var(--ink);letter-spacing:.3px}
.nav__links{display:flex;gap:32px;margin-left:62px;font-size:9.5px;font-weight:500;text-transform:uppercase;color:#333}
.nav .btn{margin-left:auto}
.hero__title{left:187px;top:212px;font-size:39px;line-height:1.02}
.hero__text{left:187px;top:308px;width:335px;font-size:10.5px;line-height:1.6}
.hero .btn{position:absolute;left:187px;top:414px}
.dots{left:187px;top:562px;display:flex;gap:13px}
.dots span{width:8px;height:8px;border-radius:50%;background:#d4d4d4}
.dots span:first-child{background:var(--teal)}
.scroll-down{left:574px;top:586px;width:52px;height:52px;border-radius:50%;background:var(--white);display:flex;align-items:center;justify-content:center}
.scroll-down div{width:42px;height:42px;border-radius:50%;background:linear-gradient(180deg,var(--blue),var(--teal));display:flex;align-items:center;justify-content:center}

/* about */
.about__map{left:187px;top:700px;width:403px;height:347px;background:linear-gradient(135deg,#e8d6b4,#d9b88f 50%,#c9a07a)}
.about__title{left:635px;top:738px;font-size:33px;line-height:1.13}
.about__text{left:635px;top:832px;width:378px;font-size:10px;line-height:1.65}
.about .btn{position:absolute;left:635px;top:970px;padding:11px 32px}

/* why */
.why{left:0;top:1135px;width:1200px;height:613px;background:linear-gradient(180deg,#cfe3ea 0%,#c4dbe3 35%,#8d8f8c 55%,#6c5e58 75%,#3f3c3d 100%)}
.why__title{left:187px;top:1198px;font-size:30px}
.why__sub{left:187px;top:1248px;font-size:11px;font-weight:700;color:var(--ink);text-transform:uppercase;letter-spacing:.4px}
.why__list{left:187px;top:1275px;list-style:none;font-size:10px;line-height:2}
.why__list li::before{content:"-  "}
.why__text{left:680px;top:1212px;width:333px;font-size:10px;line-height:1.65;text-align:right}

/* projects */
.projects__title{left:0;top:1828px;width:1200px;text-align:center;font-size:32px;line-height:1.17}
.grid{left:187px;top:1942px;width:826px;display:grid;grid-template-columns:412px 412px;grid-auto-rows:412px;gap:2px}
.tile{position:relative;display:flex;align-items:flex-end;justify-content:center;padding-bottom:40px}
.tile h3{font-family:"Unbounded",sans-serif;font-weight:900;font-size:16px;color:var(--white);text-transform:uppercase;text-align:center;line-height:1.2;letter-spacing:.3px;text-shadow:0 1px 6px rgba(0,0,0,.4)}
.t1{background:linear-gradient(180deg,#7aa6d0,#dfe7ee 40%,#2f4f7a 65%,#3e5a2c)}
.t2{background:linear-gradient(180deg,#6d8fb8,#9fbbd6 50%,#8b8a6a 75%,#4b4a35)}
.t3{background:linear-gradient(160deg,#d6e2ea,#7d97a8 45%,#27394a)}
.t4{background:linear-gradient(160deg,#4c6a3a,#7a8a62 50%,#36502c)}
.t5{background:linear-gradient(180deg,#dfe6ea,#9eb0a4 45%,#3d5a2e 75%,#2e4424)}
.t6{background:linear-gradient(160deg,#b9a98c,#8c8c8c 50%,#4a4e55)}

/* developments */
.dev{left:0;top:3255px;width:1200px;height:970px;background:var(--mint)}
.dev__title{left:187px;top:3365px;font-size:32px;line-height:1.17}
.dev__list{left:187px;top:3452px;display:flex;gap:40px;list-style:none;font-size:11px;font-weight:700;color:var(--ink)}
.dev__list li::before{content:"";display:inline-block;width:7px;height:7px;border-radius:50%;background:var(--blue);margin-right:14px;vertical-align:1px}
.dev__extra{left:187px;top:3498px;font-size:11px}
.card{padding:48px 44px;font-size:10px;line-height:1.65}
.card h3{font-family:"Unbounded",sans-serif;font-weight:900;font-size:17px;text-transform:uppercase;line-height:1.15;margin-bottom:20px;color:var(--ink)}
.card--blue{left:187px;top:3552px;width:403px;height:360px;background:var(--blue);color:var(--white)}
.card--blue h3{color:var(--white)}
.card--pale{left:608px;top:3552px;width:405px;height:360px;background:var(--pale)}
.card--wide{left:187px;top:3933px;width:826px;height:207px;background:var(--pale)}
.card--wide p+p{margin-top:12px}

/* layout */
.lot{left:0;top:4225px;width:1200px;height:425px;background:var(--grey)}
.lot__plan{left:0;top:4225px;width:600px;height:422px;background:linear-gradient(135deg,#7d8a68,#9aa587 40%,#6f7560 70%,#8a8e78)}
.lot__title{left:660px;top:4347px;font-size:32px;line-height:1.2}
.lot__text{left:660px;top:4455px;width:320px;font-size:10px;line-height:1.65}

/* footer */
.footer__logo{left:187px;top:4713px;font-size:32px}
.footer__copy{left:187px;top:4780px;font-size:10px;color:#444}
.contact{left:803px;top:4712px;display:flex;align-items:center;gap:10px}
.contact__icon{width:28px;height:28px;border-radius:50%;background:#e6f7fd;display:flex;align-items:center;justify-content:center}
.contact small{display:block;font-size:8px;color:#666}
.contact strong{font-size:13px;color:var(--ink)}
.footer__nav{left:690px;top:4782px;width:323px;display:flex;justify-content:space-between;font-size:9.5px;font-weight:500;text-transform:uppercase;color:#333}
</style>
</head>
<body>

<section class="hero abs">
  <div class="hero__photo abs photo" role="img" aria-label="Rows of solar panels under a blue sky on green grass"></div>
  <nav class="nav abs">
    <span class="logo">CRESTLINE14</span>
    <div class="nav__links"><span>Home</span><span>Why Ridgeford</span><span>Lot Layout</span><span>Contact</span></div>
    <a class="btn btn--gradient" href="#">Get in touch with us</a>
  </nav>
  <h1 class="hero__title abs display">Kestrel Solar<br>Project</h1>
  <p class="hero__text abs">Lorem Ipsum is simply dummy text of the printing and typesetting industry. Lorem Ipsum has been the industry's standard dummy text ever since the 1500s, when an unknown printer took a galley of type and scrambled it to make a type specimen book.</p>
  <a class="btn btn--gradient" href="#">Get in touch with us</a>
  <div class="dots abs"><span></span><span></span><span></span><span></span><span></span></div>
</section>
<div class="scroll-down abs"><div>
  <svg width="14" height="14" viewBox="0 0 14 14"><path d="M7 2v10M3 8l4 4 4-4" stroke="#143" stroke-width="1.6" fill="none"/></svg>
</div></div>

<section class="about">
  <div class="about__map abs photo" role="img" aria-label="Historic town map of Ridgeford"></div>
  <h2 class="about__title abs display">About<br>Crestline <span class="accent">14</span></h2>
  <p class="about__text abs">The property is located on the west side of the Town of Ridgeford, a growing municipality located northeast of Larchmont, with a regional population of 13,649. The area has a very strong local economy due to its location between Larchmont and Pine Bay, but with a stronger agricultural base. It serves as the focal point for the Ashwater area, with an unemployment rate of 5.0% lower than the provincial average of 8.2%.</p>
  <a class="btn btn--gradient" href="#">Learn more</a>
</section>

<section class="why abs" role="img" aria-label="Wind turbines across rolling hills under a pale sky"></section>
<h2 class="why__title abs display">Why <span class="accent">Ridgeford?</span></h2>
<p class="why__sub abs">Location advantage</p>
<ul class="why__list abs">
  <li>Prime location to service "the province's Industrial Heartland"</li>
  <li>Lower property tax</li>
  <li>Better visibility for highway commercial</li>
</ul>
<p class="why__text abs">Located in the County of Ridgeford business area, which is currently short of product for sale or lease in both residential and commercial real estate. The area is also in a current influx of population due to its close proximity to the development occurring in the Industrial Heartland. The County of Ridgeford is a designated community under the Rural Renewal Stream (RRS) of the Regional Advantage Immigration Program.</p>

<h2 class="projects__title abs display">Major projects in Ridgeford<br><span class="accent">Service area</span></h2>
<div class="grid abs">
  <div class="tile t1" role="img" aria-label="Solar farm panels"><h3>Kestrel Solar<br>Project</h3></div>
  <div class="tile t2" role="img" aria-label="Wind turbines on open prairie"><h3>High Meadow Wind<br>Project</h3></div>
  <div class="tile t3" role="img" aria-label="Aerial view of a carbon storage site"><h3>Northline Alliance Carbon<br>Capture Storage Hub<br>(Phase 1)</h3></div>
  <div class="tile t4" role="img" aria-label="Aerial view of an air base"><h3>Pine Bay Air Base<br>Expansion</h3></div>
  <div class="tile t5" role="img" aria-label="Housing beside a forest edge"><h3>Boreal Energy First Nations<br>Housing Initiative</h3></div>
  <div class="tile t6" role="img" aria-label="Rendering of an energy storage plant"><h3>Heron Lake<br>Compressed Air Energy<br>Storage</h3></div>
</div>

<section class="dev abs"></section>
<h2 class="dev__title abs display">Recent commercial<br>developments or <span class="accent">expansions</span></h2>
<ul class="dev__list abs">
  <li>Fieldcrest</li><li>Moreau &amp; Sons Implements Ltd</li><li>Summit Heavy Equipment</li>
</ul>
<p class="dev__extra abs">True Line Contracting (Pile Driving)</p>
<article class="card card--blue abs">
  <h3>Development plans</h3>
  <p>It is currently anticipated that the process of sub-dividing the property and installing the required services to allow for sub-division will take 18 months to complete. The developer is proposing to develop the industrial park to include a truck/RV service centre including a restaurant, a truck/RV car wash and three buildings with 6 bays of office warehouse condos averaging 2,400 square feet per bay. These units will be offered for sale or lease. Presently there is no available space of this nature in the area.</p>
</article>
<article class="card card--pale abs">
  <h3>Industrial<br>condominium complex</h3>
  <p>Upon re-zoning and sub-division, the project will move forward with construction on as many as three industrial office warehouses. Each of these buildings will consist of a building footprint of roughly 14,500 SF and 6 individually titled units as part of a condo complex. Each building will be situated with highway frontage to maximize exposure, and yard space in the rear. The developer has found this to be the ideal product for small to medium-sized businesses, which is currently lacking in the Ridgeford market. They have built a similar project in Elmwood Park, known as The Prairieview Business Condominiums.</p>
</article>
<article class="card card--wide abs">
  <h3>Existing shop</h3>
  <p>The existing shop will be parcelled together with a storage yard and sold as is. This will allow for the shop to be purchased or leased along with 2-3 acres of gravelled and fenced yard space.</p>
  <p>Upon sub-division, the developers intend to sell this property for an estimated price of $1,400,000. This property is presently being leased and a Letter of Intent to purchase has been agreed to by the existing tenant.</p>
</article>

<section class="lot abs"></section>
<div class="lot__plan abs photo" role="img" aria-label="Aerial site plan showing subdivided lots along the highway"></div>
<h2 class="lot__title abs display">Appraisal lot<br><span class="accent">layout</span></h2>
<p class="lot__text abs">This Area Structure Plan is preliminary and will require modification. Provincial Transportation is considering our proposal for access to the property off Range Road 48 to alleviate significant costs related to access from Highway 14.</p>

<footer>
  <div class="footer__logo abs display">CRESTLINE<span class="accent">14</span></div>
  <p class="footer__copy abs">Copyright@2024-All Rights Reserved</p>
  <div class="contact abs">
    <div class="contact__icon"><svg width="14" height="10" viewBox="0 0 14 10"><rect x=".5" y=".5" width="13" height="9" rx="1" fill="none" stroke="#00b4e6"/><path d="M1 1l6 5 6-5" fill="none" stroke="#00b4e6"/></svg></div>
    <div><small>Email Us</small><strong>info@crestline14.com</strong></div>
  </div>
  <nav class="footer__nav abs"><span>Home</span><span>Why Ridgeford</span><span>Lot Layout</span><span>Contact</span></nav>
</footer>

</body>
</html>
```